Boutique custom software development company needs new business card

Our nearly 20 year old custom software development company would like to better include the fact that we are now providing Bitcoin services. These new services are B2B include education (how to acquire and securely hold Bitcoin) and integrating Bitcoin payments into existing ecommerce sites or other existing systems. Please keep the card clean and simple. Attached is our current design and some other files. vexalon.example

Target Market(s)

businesses owners interested in long term relationship

Industry/Entity Type

Custom software development and Bitcoin

Contact Information for Business Card

Marcus Ellwood, marcus@vexalon.example, vexalon.example, (888) 555-VEXAL

Font styles to use
Other font styles liked:
• monospace

Requirements
Must have
• double-sided
Nice to have
• clean and simple
Should not have
• physical address

```html
<!DOCTYPE html>
<html lang="en">
<head>
<meta charset="utf-8">
<title>Vexalon business card</title>
<link rel="stylesheet" href="https://fonts.googleapis.com/css2?family=Lato:wght@300;400;900&family=Arimo:wght@400;700&display=swap">
<style>
  :root {
    --orange: #d0661c;
    --blue: #2d5b9c;
    --paper: #f2f2f0;
    --ink: #1e1e1e;
    --rule: #b9b9b9;
    --backdrop: #2a2a2c;
    --white: #ffffff;
  }
  * { box-sizing: border-box; margin: 0; padding: 0; }
  html, body {
    width: 1200px; height: 874px; overflow: hidden;
    background: var(--backdrop);
  }
  .sheet {
    width: 1200px; height: 874px;
    display: flex; flex-direction: column; align-items: center; justify-content: center;
    gap: 36px;
  }
  .card {
    position: relative;
    width: 680px; height: 389px;
    overflow: hidden;
  }

  /* Front */
  .card--front {
    background: var(--orange);
    display: flex; flex-direction: column; align-items: center; justify-content: center;
    color: var(--white);
  }
  .front-brand {
    font-family: "Lato", sans-serif;
    font-weight: 900;
    font-size: 84px;
    letter-spacing: 2px;
    line-height: 1;
  }
  .front-tagline {
    font-family: "Lato", sans-serif;
    font-weight: 300;
    font-size: 25px;
    margin-top: 6px;
    letter-spacing: 0.2px;
  }
  .front-services {
    font-family: "Lato", sans-serif;
    font-weight: 400;
    font-size: 17px;
    letter-spacing: 1.5px;
    text-transform: uppercase;
    margin-top: 14px;
  }

  /* Back */
  .card--back { background: var(--paper); }
  .back-brand {
    position: absolute; left: 36px; top: 138px;
    color: var(--blue);
  }
  .back-brand__name {
    font-family: "Lato", sans-serif;
    font-weight: 900;
    font-size: 52px;
    letter-spacing: 1.5px;
    line-height: 1;
  }
  .back-brand__tagline {
    font-family: "Lato", sans-serif;
    font-weight: 400;
    font-size: 16.5px;
    margin-top: 6px;
  }
  .back-brand__services {
    font-family: "Lato", sans-serif;
    font-weight: 400;
    font-size: 14px;
    margin-top: 4px;
    color: var(--orange);
  }
  .divider {
    position: absolute; left: 366px; top: 150px;
    width: 1px; height: 112px;
    background: var(--rule);
  }
  .contact {
    position: absolute; left: 392px; top: 160px;
    font-family: "Arimo", sans-serif;
    color: var(--ink);
  }
  .contact__name {
    font-weight: 700;
    font-size: 24px;
    letter-spacing: 1px;
    margin-bottom: 12px;
  }
  .contact__first { color: var(--blue); }
  .contact__last { color: var(--orange); }
  .contact__line {
    display: flex; align-items: center; gap: 8px;
    font-size: 19px;
    line-height: 1.45;
  }
  .contact__icon { width: 17px; height: 17px; flex: none; }
  .footer-band { position: absolute; left: 0; bottom: 0; width: 680px; height: 44px; }
  .website {
    position: absolute; right: 28px; bottom: 9px;
    font-family: "Arimo", sans-serif;
    font-size: 17px;
    letter-spacing: 1px;
    color: var(--white);
  }
</style>
</head>
<body>
<main class="sheet">
  <section class="card card--front">
    <div class="front-brand">VEXALON</div>
    <div class="front-tagline">developer of custom applications</div>
    <div class="front-services">Bitcoin payments &amp; education</div>
  </section>

  <section class="card card--back">
    <div class="back-brand">
      <div class="back-brand__name">VEXALON</div>
      <div class="back-brand__tagline">developer of custom applications</div>
      <div class="back-brand__services">Bitcoin payments &amp; education for business</div>
    </div>
    <div class="divider"></div>
    <div class="contact">
      <div class="contact__name"><span class="contact__first">MARCUS</span> <span class="contact__last">ELLWOOD</span></div>
      <div class="contact__line">
        <svg class="contact__icon" viewBox="0 0 17 17" aria-hidden="true">
          <rect width="17" height="17" rx="2" fill="var(--orange)"/>
          <path d="M5 3.5l2 2.5-1.2 1.3c.8 1.6 2 2.8 3.5 3.6L10.6 9.6 13 11.6 11.8 13.6C8 13 4 9 3.4 5z" fill="var(--white)"/>
        </svg>
        <span>(888) 555-VEXAL</span>
      </div>
      <div class="contact__line">
        <svg class="contact__icon" viewBox="0 0 17 17" aria-hidden="true">
          <rect width="17" height="17" rx="2" fill="var(--orange)"/>
          <rect x="3.5" y="5" width="10" height="7.5" fill="none" stroke="var(--white)" stroke-width="1.2"/>
          <path d="M3.5 5l5 4 5-4" fill="none" stroke="var(--white)" stroke-width="1.2"/>
        </svg>
        <span>marcus@vexalon.example</span>
      </div>
    </div>
    <svg class="footer-band" viewBox="0 0 680 44" aria-hidden="true">
      <rect x="0" y="34" width="420" height="10" fill="var(--blue)"/>
      <polygon points="385,44 415,8 680,8 680,44" fill="var(--orange)"/>
    </svg>
    <div class="website">www.vexalon.example</div>
  </section>
</main>
</body>
</html>
```